Business card for a shipping supplies business

Needing a business card design. Please see the logo. The logo with the white font should be used if there is a dark background.

We are looking for the following info on the card. Please see the sample info. We will need the info to be changed with a few different employee names and info but all will use the same template.

Business Name: The Crate Heron
Employee Name : Marcus Delaney
Position: Account Manager
Address: 4827 W. Ridge 418 S.
Fort Worth, TX 73948
email: Marcus@thecrateheron.example
telephone: 855-619-2740 x 207
website: www.getparcelkits.example

Target Market(s)

Businesses who ship products for online sales

Industry/Entity Type

Cardboard

Contact Information for Business Card

Name, title, address, website, logo, telephone number

Font styles to use
Sans Serif

Colors
EE7325
F08F49
F5BC92
FAE3D3
FDF4ED

Requirements
Must have
• Logo on back of card. Clean look, just logo, website address

```html
<!DOCTYPE html>
<html lang="en">
<head>
<meta charset="utf-8">
<title>The Crate Heron – Business Card</title>
<link rel="stylesheet" href="https://fonts.googleapis.com/css2?family=Montserrat:wght@600;700&family=Roboto:wght@400;500&display=swap">
<style>
  :root {
    --orange: #EE7325;
    --orange-soft: #F08F49;
    --card: #1c1b1b;
    --backdrop: #2b2b2b;
    --white: #ffffff;
    --rule: #8a8a8a;
  }
  * { box-sizing: border-box; margin: 0; padding: 0; }
  html, body { width: 1200px; height: 800px; overflow: hidden; }
  body {
    background: var(--backdrop);
    font-family: "Roboto", Arial, sans-serif;
    color: var(--white);
    position: relative;
  }
  .card {
    position: absolute;
    background: var(--card);
    box-shadow: 0 18px 40px rgba(0,0,0,.55);
  }
  .card--back { left: 90px; top: 50px; width: 600px; height: 343px; }
  .card--front { left: 500px; top: 390px; width: 640px; height: 366px; }

  .brand { display: flex; align-items: center; gap: 12px; }
  .brand__mark { width: 22px; height: 22px; border-radius: 50%; background: var(--orange); flex: none; }
  .brand__name {
    font-family: "Montserrat", Arial, sans-serif;
    font-weight: 700;
    color: var(--white);
    letter-spacing: 1px;
    text-transform: uppercase;
  }

  .card--back .brand { position: absolute; left: 0; right: 0; top: 130px; justify-content: center; }
  .card--back .brand__name { font-size: 40px; }
  .back-url {
    position: absolute; left: 0; right: 0; top: 215px;
    text-align: center; font-size: 15px; letter-spacing: 4px; color: var(--white);
  }
  .back-url span { color: var(--orange); }

  .card--front .brand { position: absolute; right: 40px; top: 62px; }
  .card--front .brand__name { font-size: 34px; }
  .rule-top { position: absolute; left: 0; right: 26px; top: 142px; height: 1px; background: var(--rule); }

  .person { position: absolute; left: 40px; top: 196px; padding-left: 16px; border-left: 5px solid var(--orange); }
  .person__name {
    font-family: "Montserrat", Arial, sans-serif; font-weight: 700;
    font-size: 27px; color: var(--orange); text-transform: uppercase; line-height: 1.05;
  }
  .person__title { font-size: 17px; margin-top: 4px; }
  .rule-mid { position: absolute; left: 60px; width: 240px; top: 270px; height: 1px; background: var(--rule); }

  .contact { position: absolute; left: 60px; top: 284px; list-style: none; font-size: 17px; line-height: 24px; }
  .contact li { display: flex; align-items: center; gap: 10px; }
  .contact svg { width: 14px; height: 14px; fill: var(--orange); flex: none; }

  .address { position: absolute; right: 40px; top: 170px; font-size: 17px; line-height: 23px; text-align: left; }
  .address__company { color: var(--orange); text-transform: uppercase; }
</style>
</head>
<body>
  <section class="card card--back" aria-label="Card back">
    <div class="brand">
      <span class="brand__mark"></span>
      <span class="brand__name">Crate Heron</span>
    </div>
    <p class="back-url">www.<span>getparcelkits</span>.example</p>
  </section>

  <section class="card card--front" aria-label="Card front">
    <div class="brand">
      <span class="brand__mark"></span>
      <span class="brand__name">Crate Heron</span>
    </div>
    <div class="rule-top"></div>

    <div class="person">
      <h1 class="person__name">Marcus Delaney</h1>
      <p class="person__title">Account Manager</p>
    </div>
    <div class="rule-mid"></div>

    <ul class="contact">
      <li>
        <svg viewBox="0 0 24 24" aria-hidden="true"><path d="M6.6 10.8a15 15 0 0 0 6.6 6.6l2.2-2.2c.3-.3.7-.4 1-.2 1.1.4 2.3.6 3.6.6.6 0 1 .4 1 1V20c0 .6-.4 1-1 1A17 17 0 0 1 3 4c0-.6.4-1 1-1h3.5c.6 0 1 .4 1 1 0 1.3.2 2.5.6 3.6.1.3 0 .7-.2 1z"/></svg>
        855-619-2740 x 207
      </li>
      <li>
        <svg viewBox="0 0 24 24" aria-hidden="true"><path d="M2 5h20v14H2zm2 2v.5l8 5 8-5V7l-8 5z"/></svg>
        Marcus@thecrateheron.example
      </li>
      <li>
        <svg viewBox="0 0 24 24" aria-hidden="true"><path d="M12 2a10 10 0 1 0 0 20 10 10 0 0 0 0-20zm6.9 6h-3a15 15 0 0 0-1.4-3.6A8 8 0 0 1 18.9 8zM12 4c.8 1.2 1.5 2.5 1.9 4h-3.8c.4-1.5 1.1-2.8 1.9-4zM4.3 14a8 8 0 0 1 0-4h3.4a16 16 0 0 0 0 4zm.8 2h3a15 15 0 0 0 1.4 3.6A8 8 0 0 1 5.1 16zm3-8h-3a8 8 0 0 1 4.4-3.6C8.9 5.6 8.4 6.7 8.1 8zM12 20c-.8-1.2-1.5-2.5-1.9-4h3.8c-.4 1.5-1.1 2.8-1.9 4zm2.3-6H9.7a14 14 0 0 1 0-4h4.6a14 14 0 0 1 0 4zm.2 5.6c.6-1.1 1.1-2.3 1.4-3.6h3a8 8 0 0 1-4.4 3.6zm1.8-5.6a16 16 0 0 0 0-4h3.4a8 8 0 0 1 0 4z"/></svg>
        www.getparcelkits.example
      </li>
    </ul>

    <address class="address" style="font-style:normal">
      <span class="address__company">The Crate Heron</span><br>
      4827 W. Ridge 418 S.<br>
      Fort Worth, TX 73948
    </address>
  </section>
</body>
</html>
```